Design Our Camera Package Graphic Must Be Awesome! We Have Lots More Work!

We want the attached graphic redesigned to feature our camera packages instead of the the home theater package. The information to be included in the package you can find in the second attachment. We have also included our logo. We want a really nice graphic the winner will have to make 3 graphic all with exact layout but slightly different see our website for an example http://brixtonlanefitters.example/home-theater-packages/#.VUPmopPz7zw. Remember this design will be built around the attached file named: Package Graphic info. Your design must standout. If you do really good job we will have a lot more work for you in the future. .

Target Market(s)

Home Owners

Industry/Entity Type

Camera

Font styles to use
Sans Serif

Colors
0255a3
33a6d7
85acd3
3277b5
ffffff

Requirements
Must have
• Pictures of dome cameras and bullet cameras, dvr, our company logo and MUST LOOK AWESOME!
Should not have
• We have included an example of what we are not looking for

```html
<!DOCTYPE html>
<html lang="en">
<head>
<meta charset="utf-8">
<title>4 Camera Packages – Brixton Lane Fitters</title>
<link href="https://fonts.googleapis.com/css2?family=Arimo:wght@400;700&display=swap" rel="stylesheet">
<style>
  :root{
    --navy:#0b3f78;
    --blue:#0255a3;
    --blue-mid:#3277b5;
    --sky:#33a6d7;
    --pale:#85acd3;
    --white:#ffffff;
    --ink:#1f2f45;
    --price-a:#e4572e;
    --price-b:#b52a17;
    --room-a:#e9e6e1;
    --room-b:#bfb7ad;
  }
  *{box-sizing:border-box;margin:0;padding:0}
  html,body{width:849px;height:1200px;overflow:hidden;background:var(--white)}
  body{font-family:"Arimo",Arial,sans-serif;color:var(--ink)}
  .poster{position:relative;width:849px;height:1200px;overflow:hidden;background:var(--white)}

  .hero-photo{position:absolute;left:0;top:0;width:849px;height:432px;
    background:linear-gradient(180deg,#f3f1ee 0%,#d9d3cb 55%,#a9a39c 100%)}
  .brand{position:absolute;left:292px;top:0;width:265px;height:92px;background:var(--white);
    display:flex;flex-direction:column;align-items:center;justify-content:center;gap:8px;
    box-shadow:0 2px 6px rgba(0,0,0,.15)}
  .brand-name{font-weight:700;font-size:19px;color:var(--navy);letter-spacing:.5px;white-space:nowrap}
  .brand-line{width:200px;height:3px;background:var(--sky)}

  .product-photo{position:absolute;left:335px;top:320px;width:240px;height:100px;border-radius:10px;z-index:3;
    background:linear-gradient(180deg,#5a6068 0%,#2c3037 60%,#1b1e23 100%)}

  .pkg{position:absolute;top:432px;width:424.5px;height:493px;z-index:2}
  .pkg-basic{left:0;background:var(--white);padding:16px 40px 0 40px}
  .pkg-equip{left:424.5px;
    background:linear-gradient(180deg,var(--blue-mid) 0%,var(--blue) 100%);color:var(--white);padding:18px 28px 0 40px}
  .pkg-title{font-weight:700;font-size:30px;text-transform:uppercase}
  .pkg-basic .pkg-title{line-height:51px}
  .pkg-equip .pkg-title{line-height:40px;text-align:center}
  .includes{font-size:22px;font-weight:700;margin:10px 0 10px}
  .pkg-equip .includes{margin-top:16px}
  .list{list-style:none}
  .list li{font-size:14px;line-height:1.2;padding:0 0 0 22px;position:relative}
  .pkg-basic .list li{height:40px}
  .pkg-equip .list li{height:32px}
  .list li::before{content:"";position:absolute;left:0;top:2px;border:6px solid transparent;
    border-left:8px solid var(--sky)}
  .pkg-equip .list li::before{border-left-color:var(--white)}

  .room-photo{position:absolute;left:0;top:925px;width:849px;height:85px;
    background:linear-gradient(180deg,#e4e1dc 0%,var(--room-a) 40%,var(--room-b) 100%)}
  .price{position:absolute;top:937px;width:200px;height:60px;border-radius:30px;z-index:3;
    background:linear-gradient(180deg,var(--price-a),var(--price-b));color:var(--white);
    font-weight:700;font-size:38px;display:flex;align-items:center;justify-content:center;
    box-shadow:0 3px 8px rgba(0,0,0,.3)}
  .price sup{font-size:16px;margin-left:2px}
  .price-basic{left:112px}
  .price-equip{left:565px}

  .excludes{position:absolute;left:0;top:1010px;width:849px;height:190px;background:var(--navy);
    color:var(--white);display:flex}
  .exclude-col{width:50%;padding:16px 20px 0 20px}
  .exclude-col+.exclude-col{border-left:1px solid var(--blue-mid)}
  .exclude-col h3{font-size:24px;font-weight:700;margin-bottom:18px}
  .excludes .list li{font-size:14px;height:40px}
</style>
</head>
<body>
<main class="poster">
  <div class="hero-photo" role="img" aria-label="Photo of a bright modern living room with a wall-mounted flat screen"></div>
  <header class="brand">
    <span class="brand-name">BRIXTON LANE FITTERS</span>
    <span class="brand-line"></span>
  </header>

  <div class="product-photo" role="img" aria-label="Four dome security cameras above a digital video recorder"></div>

  <section class="pkg pkg-basic">
    <h2 class="pkg-title">4 Camera<br>Installation<br>Package</h2>
    <h3 class="includes">Includes:</h3>
    <ul class="list">
      <li>Conduct a site survey and explain installation</li>
      <li>Unpack Your Camera/DVR system</li>
      <li>Mount and Secure your Cameras</li>
      <li>Conceal Writing from mount to DVR viewing room</li>
      <li>Program Basic Functions on the DVR</li>
      <li>Tutorial on basic features of your new system</li>
      <li>Clean up work area and remove Installation debris</li>
    </ul>
  </section>

  <section class="pkg pkg-equip">
    <h2 class="pkg-title">4 Camera<br>Installation with<br>Equipment</h2>
    <h3 class="includes">Includes:</h3>
    <ul class="list">
      <li>Conduct a site survey and explain installation</li>
      <li>Mount and Secure your Cameras</li>
      <li>Conceal Wiring from mount to DVR viewing room</li>
      <li>Program Basic functions on the DVR</li>
      <li>Tutorial on basic features of your new system</li>
      <li>Clean up work area and remove installation debris</li>
      <li>4 night vision/color cameras</li>
      <li>4 sets of 60ft connection cables (.30c per foot after)</li>
      <li>4 Channel Digital Video Recorder</li>
    </ul>
  </section>

  <div class="room-photo" role="img" aria-label="Photo of a furnished living room with sofa and lamp"></div>
  <div class="price price-basic">$399<sup>99</sup></div>
  <div class="price price-equip">$999<sup>99</sup></div>

  <footer class="excludes">
    <div class="exclude-col">
      <h3>Does not Includes:</h3>
      <ul class="list">
        <li>Equipment or wiring</li>
        <li>network Set-up for remote Viewing ($100 additional)</li>
      </ul>
    </div>
    <div class="exclude-col">
      <h3>Does not Includes:</h3>
      <ul class="list">
        <li>Viewing monitor</li>
        <li>network Set-up for remote Viewing ($100 additional)</li>
      </ul>
    </div>
  </footer>
</main>
</body>
</html>
```